Specialist Medical practice after professional trifold flyer design for patient information brochure

I am the Director of the Hollowbrook Clinic, a specialist medial and surgical practice in Australia. I am after a professional design of a patient information trifold flyer that can be used for web distribution or for commercial printing for upcoming educational event. The design would need to allow change of images and text to be used as template for future topics but have a common brand look across them. Colours would follow the logo, but primarily blue colours for the hollowbrook theme. The inside text needs to be clearly contrasted to the background for easy reading, as often elderly patients. The design would make use of curves or circles, but open for hexagonal, triangle square vector components. I have included an outline for the initial brochure and included images to include. Other stock background images can be used if they increase the impact of the design over included. A winning design is also one that could be modified to a 4 page bi-fold brochure

Target Market(s)

This will be provided to patients in GP practices, podiatry clinics, radiological practices. Aimed at patients to read and be compelled to look to site or get consultation with me

Industry/Entity Type

Medical

Font styles to use
Serif
Sans Serif

Colors
33a6d7
0355a3
86cfc6
cedeed
0292cd
85cae6

Requirements
Must have
• The front cover needs to engage the patient to pick up and read- yes I have a painful ankle and want to find out more. the goal for the inside is to provide the options but be able to direct to website for more info - website currently undergoing upgrade. After professional modern look. Not bright contrasting colours like many advertising brochures. Needs to able to have images and text changed but following same look to create new topics
Nice to have
• The focus is a Tri-fold brochure. Nice to be able to modify to bifold. A winning design would even offer both, or submit separate bifold and trifold. I am open to different versions of similar look. (eg option of brochure with curved elements, triangular or square, or hexagonal.
Should not have
• To many contrasting colours. Text must be easily read on background, either white or coloured background texture with transparency

```html
<!DOCTYPE html>
<html lang="en">
<head>
<meta charset="utf-8">
<title>My Painful Ankle – Hollowbrook Clinic</title>
<link href="https://fonts.googleapis.com/css2?family=Arimo:ital,wght@0,400;0,700;1,400;1,700&display=swap" rel="stylesheet">
<style>
  :root{
    --navy:#0355a3;
    --deep:#0a4f9c;
    --sky:#33a6d7;
    --bright:#0292cd;
    --pale:#85cae6;
    --mist:#cedeed;
    --sun:#f3e24a;
    --white:#ffffff;
  }
  *{margin:0;padding:0;box-sizing:border-box}
  html,body{width:1200px;height:933px;overflow:hidden;background:#fff}
  body{font-family:"Arimo",Arial,sans-serif}
  .brochure{position:relative;width:1200px;height:933px;overflow:hidden;background:var(--white)}
  .shapes{position:absolute;inset:0;width:1200px;height:933px}
  .photo{position:absolute}
  .photo--surgeon{left:60px;top:20px;width:300px;height:372px;background:linear-gradient(180deg,#e9eef3 0%,#c9d3de 45%,#2a2f38 70%,#1c2129 100%)}
  .photo--hospital{left:406px;top:15px;width:392px;height:373px;background:linear-gradient(180deg,#5d84b8 0%,#9db6d6 45%,#e8ecef 70%,#6b7468 100%)}
  .photo--ankle{left:802px;top:0;width:398px;height:500px;background:linear-gradient(160deg,#f7e6b5 0%,#e6c48b 40%,#c39a5e 75%,#9a7a4c 100%)}

  .profile{position:absolute;left:40px;top:420px;width:350px;color:var(--pale);font-size:13.4px;line-height:16.3px}
  .profile__name{font-size:24px;font-weight:700;color:var(--pale);margin-bottom:22px}
  .profile__heading{font-weight:700;margin:24px 0 22px}
  .profile__lead{color:var(--sun);font-weight:700;font-style:italic}
  .profile__list{list-style:none;margin-top:2px;color:var(--sun)}
  .profile__list li{position:relative;padding-left:12px}
  .profile__list li::before{content:"";position:absolute;left:1px;top:6px;width:5px;height:5px;border-radius:50%;background:var(--sun)}
  .profile__list em{font-style:italic}

  .contact{position:absolute;left:404px;width:392px;text-align:center;color:var(--navy);font-size:14px}
  .contact__icon{position:absolute;left:588px;width:30px;height:30px}
  .address{position:absolute;left:404px;top:852px;width:392px;text-align:center;color:var(--pale);font-size:13.4px;line-height:20px}
  .address em{font-style:italic}

  .cover-title{position:absolute;left:800px;top:570px;width:400px;text-align:center;color:var(--navy);font-weight:700;line-height:1}
  .cover-title__big{display:block;font-size:45px;letter-spacing:.5px}
  .cover-title__sub{display:block;font-size:17px;margin-top:2px}
  .surgeon{position:absolute;left:800px;top:762px;width:400px;text-align:center;color:var(--pale)}
  .surgeon__name{font-size:30px;font-weight:700;margin-bottom:6px}
  .surgeon__role{font-size:24px;line-height:35px}
</style>
</head>
<body>
<main class="brochure">
  <div class="photo photo--surgeon" role="img" aria-label="Portrait photograph of the surgeon in a dark suit"></div>
  <div class="photo photo--hospital" role="img" aria-label="Photograph of the modern private hospital building against a blue sky"></div>
  <div class="photo photo--ankle" role="img" aria-label="Photograph of a person holding a sore ankle outdoors in warm sunlight"></div>

  <svg class="shapes" viewBox="0 0 1200 933" preserveAspectRatio="none" aria-hidden="true">
    <polygon points="968,0 1200,0 1200,45" fill="var(--navy)"/>
    <polygon points="15,392 800,392 1200,445 1200,498 800,500 404,465 404,920 15,920" fill="var(--deep)"/>
    <polygon points="404,465 800,500 1200,495 1200,716 800,762 800,845 404,845" fill="var(--sky)"/>
    <polygon points="800,502 1200,498 1200,716 800,762" fill="#4fb3dd"/>
    <polygon points="404,845 800,845 800,920 404,920" fill="var(--navy)"/>
    <polygon points="800,762 1200,716 1200,920 800,920" fill="var(--navy)"/>
  </svg>

  <section class="profile">
    <h2 class="profile__name">Dr Marcus Hale</h2>
    <p>MBBS (Hons), FRACS (Ortho), FA (Ortho)<br>
    Dr Marcus Hale is an Australian trained Orthopaedic Surgeon who has a primary focus in the treatment of conditions of the foot and ankle. He has completed post fellowship training in Foot and Ankle surgery both locally and internationally, and continues to update himself in the latest techniques.</p>
    <h3 class="profile__heading">Conditions treated</h3>
    <p><span class="profile__lead">Dr Hale provides assessment and treatment of all foot</span><br>and ankle conditions. He has special interest in the</p>
    <ul class="profile__list">
      <li>Minimally invasive treatment for bunions and toe deformities.</li>
      <li>Joint sparing procedures for arthritis or deformity, including the Arcline implant.</li>
      <li>Joint fusion procedures for arthritis of the feet and ankle</li>
      <li>Sports injuries and tendinopathies.</li>
      <li>Total ankle replacement and deformity correction of the <em>foot and ankle.</em></li>
    </ul>
  </section>

  <svg class="contact__icon" style="top:518px" viewBox="0 0 30 30" aria-hidden="true"><circle cx="15" cy="15" r="14" fill="var(--navy)"/><path d="M8 12c2-3 12-3 14 0l-2 2-2-1v-1h-6v1l-2 1zM10 15h10l1 6H9z" fill="#fff"/></svg>
  <p class="contact" style="top:553px">(02) 5550 1234</p>

  <svg class="contact__icon" style="top:607px" viewBox="0 0 30 30" aria-hidden="true"><circle cx="15" cy="15" r="14" fill="var(--navy)"/><rect x="11" y="8" width="8" height="5" fill="#fff"/><rect x="8" y="13" width="14" height="7" rx="1" fill="#fff"/><rect x="11" y="18" width="8" height="4" fill="var(--navy)" stroke="#fff"/></svg>
  <p class="contact" style="top:642px">(02) 5550 5678</p>

  <svg class="contact__icon" style="top:700px" viewBox="0 0 30 30" aria-hidden="true"><circle cx="15" cy="15" r="14" fill="var(--navy)"/><rect x="8" y="10" width="14" height="10" rx="1" fill="#fff"/><path d="M8 10l7 6 7-6" fill="none" stroke="var(--navy)" stroke-width="1.2"/></svg>
  <p class="contact" style="top:730px">info@hollowbrookclinic.com.au</p>

  <svg class="contact__icon" style="top:788px" viewBox="0 0 30 30" aria-hidden="true"><circle cx="15" cy="15" r="14" fill="var(--navy)"/><g fill="none" stroke="#fff" stroke-width="1.3"><circle cx="15" cy="15" r="7"/><ellipse cx="15" cy="15" rx="3" ry="7"/><path d="M8 15h14M9.5 11h11M9.5 19h11"/></g></svg>
  <p class="contact" style="top:820px">www.hollowbrookclinic.com.au</p>

  <address class="address"><em>Suite 701, Level 7, Kestrel Private Hospital</em><br>128-132 Harbour St, Marlow Bay NSW<br>45 River Road, Elmsford NSW</address>

  <h1 class="cover-title">
    <span class="cover-title__big">MY</span>
    <span class="cover-title__big">PAINFUL ANKLE</span>
    <span class="cover-title__sub">SOLUTIONS FOR ANKLE ARTHRITIS</span>
  </h1>

  <section class="surgeon">
    <p class="surgeon__name">Dr Marcus Hale</p>
    <p class="surgeon__role">Orthopaedic Foot<br>&amp;<br>Ankle Surgeon</p>
  </section>
</main>
</body>
</html>
```